Conservative, Modern and Sharp Builder Business card

Hi there,
We would like to update our existing business card.
I have attached photos of existing business card, logo and van sign.

I would like the business card to also list what we do :
Renovation • New Build • Alteration
Extension • Bathroom • Maintenance.(Seperated by dots)

Contact number : 021 0483 0752
(With that exact spacing)

Ideally when people looking from about 2-3 metres, they know that it is a builder’s business card

Open to suggestions on fonts, layout, style of business card

PLEASE ONLY SUBMIT YOUR BEST OR MAX 3 DESIGNS FOR EACH DESIGNER

Thanks

Industry/Entity Type

Construction. Renovation

Contact Information for Business Card

Details should be the same as the existing card. And addition of what we do.

Requirements
Should not have
• The new business card must not have the same layout as our existing one. Thanks

```html
<!DOCTYPE html>
<html lang="en">
<head>
<meta charset="utf-8">
<title>KeelBuild Business Card</title>
<link href="https://fonts.googleapis.com/css2?family=Lato:wght@400;700;900&display=swap" rel="stylesheet">
<style>
  :root {
    --ink: #0b0b0b;
    --paper: #ffffff;
    --muted: #555555;
    --backdrop: #2a2a2a;
  }
  * { margin: 0; padding: 0; box-sizing: border-box; }
  html, body { width: 1200px; height: 900px; overflow: hidden; }
  body {
    background: var(--backdrop);
    font-family: "Lato", sans-serif;
    display: flex;
    flex-direction: column;
    align-items: center;
    justify-content: center;
    gap: 40px;
  }
  .card {
    position: relative;
    width: 640px;
    height: 366px;
    border-radius: 22px;
    overflow: hidden;
  }
  .card-front {
    background: var(--ink);
    color: var(--paper);
    display: flex;
    flex-direction: column;
    align-items: center;
    justify-content: center;
  }
  .brand {
    display: flex;
    align-items: center;
    gap: 14px;
    margin-top: 10px;
  }
  .brand-mark {
    width: 26px;
    height: 26px;
    background: var(--paper);
  }
  .brand-name {
    font-weight: 900;
    font-size: 76px;
    letter-spacing: -1px;
    line-height: 1;
  }
  .services {
    margin-top: 48px;
    font-size: 17px;
    letter-spacing: 0.3px;
    white-space: nowrap;
  }
  .card-back { background: var(--paper); color: var(--ink); }
  .holder {
    position: absolute;
    left: 52px;
    top: 60px;
  }
  .holder-name {
    font-weight: 900;
    font-size: 34px;
    letter-spacing: 1px;
    line-height: 1.1;
  }
  .holder-role {
    font-size: 20px;
    color: var(--muted);
    margin-top: 4px;
    letter-spacing: 0.5px;
  }
  .contact-band {
    position: absolute;
    left: 0;
    right: 0;
    bottom: 0;
    height: 160px;
    background: var(--ink);
  }
  .contact-list {
    position: absolute;
    right: 28px;
    bottom: 20px;
    list-style: none;
    color: var(--paper);
    text-align: right;
  }
  .contact-item {
    display: flex;
    align-items: center;
    justify-content: flex-end;
    gap: 12px;
    font-size: 17px;
    line-height: 29px;
  }
  .contact-item.phone { font-size: 22px; font-weight: 700; letter-spacing: 1px; }
  .contact-icon { width: 18px; height: 18px; flex: none; }
</style>
</head>
<body>
  <section class="card card-front">
    <div class="brand">
      <span class="brand-mark"></span>
      <span class="brand-name">KeelBuild</span>
    </div>
    <p class="services">Renovation • New Build • Alteration • Extension • Bathroom • Maintenance</p>
  </section>

  <section class="card card-back">
    <div class="holder">
      <h1 class="holder-name">TOMAS REYES</h1>
      <p class="holder-role">Residential Builder</p>
    </div>
    <div class="contact-band"></div>
    <ul class="contact-list">
      <li class="contact-item phone">021 0483 0752
        <svg class="contact-icon" viewBox="0 0 24 24" fill="none" stroke="#fff" stroke-width="2"><path d="M5 3h4l2 5-3 2a12 12 0 0 0 6 6l2-3 5 2v4a2 2 0 0 1-2 2A18 18 0 0 1 3 5a2 2 0 0 1 2-2z"/></svg>
      </li>
      <li class="contact-item">KeelBuild@mailhub.co
        <svg class="contact-icon" viewBox="0 0 24 24" fill="none" stroke="#fff" stroke-width="2"><rect x="3" y="5" width="18" height="14"/><path d="M3 5l9 8 9-8"/></svg>
      </li>
      <li class="contact-item">www.KeelBuild.co.nz
        <svg class="contact-icon" viewBox="0 0 24 24" fill="none" stroke="#fff" stroke-width="2"><circle cx="12" cy="12" r="9"/><path d="M3 12h18M12 3c3 3 3 15 0 18M12 3c-3 3-3 15 0 18"/></svg>
      </li>
      <li class="contact-item">@KeelBuild.nz
        <svg class="contact-icon" viewBox="0 0 24 24" fill="none" stroke="#fff" stroke-width="2"><circle cx="12" cy="12" r="8"/></svg>
      </li>
    </ul>
  </section>
</body>
</html>
```